Can you make FairlyNeat look better than average? We need business cards and a logo refresh :-)

REVISED BRIEF

PRIORITY

VECTOR LOGO

Create a vector version of our existing logo. The logo must not change from its current design, weight or font.

Deliverables

- Logo in blue (#2540BB)
- Logo in white (#FFFFFF)
- Logo in grey (#36454F)
- All logos on transparent background
- All logos in PNG & SVG formats. (SVG must NOT distort stroke width when resized)

BRAND MARK

Create a brand mark for use with the logo. This should be possible to used with the logo and on its own as a stand alone graphical device that represents the FairlyNeat brand.

https://pagewrightly.com/resources/glossary/what-is-a-brand-mark

Deliverables

- Brand Mark in blue (#2540BB)
- Brand Mark in white (#FFFFFF)
- Brand Mark in grey (#36454F)
- Brand Mark on transparent background
- Brand Mark in PNG & SVG formats. (SVG must NOT distort stroke width when resized)
- Logo combined with Brand Mark (colours and formats)
.

Business Card Layout

Create 2 layouts with the following details:-

Marcus Thorne
Co-Founder & Chief Product Officer

marcus@fairlyneat.nz
www.fairlyneat.nz
0279183640

Duncan Wells
Founder & CEO

hello@fairlyneat.nz
www.fairlyneat.nz
021 468 9271

DESIGN CONSIDERATIONS

Create versions with ‘Shaping Labels With Heart’ tag line incorporated within the design and without (maintain separation of logo from tag line)

- Create a version with and without the brand mark
- Keep it clean and simple but elevate the design with subtle design effects
- Consider use of raised spot gloss colour (this can be white on white for subtle or blue on blue or blue on white)
- Consider use of spot gloss colour (this can be white on white for subtle or blue on blue or blue on white)
- Consider use of letterpress indentation
- Ensure contact details are legible, use sans-serif font

PREVIOUS BRIEF

We need a business card design for our business FairlyNeat. We are a purpose driven brand and media agency that helps brands and charities plan and buy traditional media campaigns (TV, Radio, Print, Outdoor etc). We give a significant amount of the media booking fees we receive from media vendors to charity in the name of our clients. https://www.linkedin.com/posts/wearefairlyneat_giveback-fairlyneat-shapinglabelswithheart-activity-7000000000000000000-Xqzt

Our strapline is 'Shaping Labels With Heart'.

We want to keep our logo design as it is but it does need tightening up and made into a proper vector image as it's been created from a font.

Our brand colour is #2540BB and we need to keep this.

Our brand is professional but human, warm and engaging and doesn't take itself too seriously.

Things We Need
- vectorisation and tidying up of existing logo
- We'd like you to think about how we can incorporate a brand mark with the logo to add another dimension to our brand
- business card layout and design
- we'll be using printzo.com to print the cards so please take a look at the options they have (spot gloss, foil, letterpress, square cards and even the backs of the cards can have a different design on every single card!
- potential opportunity for different famous quotes on the back or imagery or slight design differences
- we'd be open to the use of an emoji or emojiis as the brandmark or to be incorporated into the card designs
- we can have as many different design batches as we like for the backs of the cards

https://www.printzo.com/au/business-cards

We want to make an impact, we want to be seen as professional but fun, we want to be different.

Here's a press release of what we're about.

https://adwirenews.co.nz/movings-shakings/fairlyneat-welcomes-marcus-thorne-as-co-founder/

Be bold, be different, there is no such thing as a bad idea. We're open to anything so please bring your best ideas and have fun with it! Go crazy if you like!
____________
Marcus Thorne
marcus@fairlyneat.nz
0279183640

Duncan Wells
Founder & CEO
hello@fairlyneat.nz
021 468 9271

Shaping Labels With Heart

________

These are the only details we MUST have on the cards, the rest is up to you. Just make sure you use all of your creativity but don't feel the need to crowd the card with too much, let it breathe as well.

In terms of font for the details, we'll leave that up to you, just ensure it's legible. Oh and please don't take any design inspiration from our website - that will be changing!

Please don't let the design and layout look cheap and tacky though. It needs to still feel premium but personable.

Thanks

Marcus
Updates

Many designs are changing the logo and this was NOT in the brief. We need a brand mark to complement the logo. We need to see the logo with and without the brand mark. We need to see the business card with both logo + brand mark and logo on its own We need to see the business card with and without the tagline 'Shaping Labels With Heart'

Industry/Entity Type

purpose driven Brand & Media Agency

Contact Information for Business Card

Shaping Labels With Heart
Marcus Thorne, Co-Founder & Chief Product Officer, marcus@fairlyneat.nz fairlyneet.nz, 0279 183 640

Duncan Wells, Founder & CEO hello@fairlyneat.nz, fairlyneet.nz, 021 468 9271

Font styles to use
Serif
Sans Serif

Colors
0054AA
0677BA
7BADD7
CADEEF
E8F1F8

Requirements
Must have
• brand mark, vector version of existing logo, Shaping Labels With Heart tagline, existing logo traced and vectorised. Must fully explore the design options from printzo.com that can enhance the overall card design
Nice to have
• brandmark to help elevate the logo, maybe incorporate some other design elements into the card like lines, or grids.
Should not have
• A cheap look and feel

```html
<!DOCTYPE html>
<html lang="en">
<head>
<meta charset="utf-8">
<title>FairlyNeat Business Card</title>
<link rel="stylesheet" href="https://fonts.googleapis.com/css2?family=Noto+Sans:wght@400&display=swap">
<style>
  :root {
    --brand-blue: #2540BB;
    --card-blue: #1C30A8;
    --paper: #F6F6F6;
    --ink-grey: #5E5E5E;
    --rule-grey: #6A6A6A;
    --backdrop: #9A9A9A;
    --white: #FFFFFF;
    --edge-light: #E4E4E4;
  }
  * { margin: 0; padding: 0; box-sizing: border-box; }
  html, body {
    width: 1200px;
    height: 1050px;
    overflow: hidden;
    background: var(--backdrop);
    font-family: "Noto Sans", sans-serif;
  }
  .stage {
    position: relative;
    width: 1200px;
    height: 1050px;
  }
  .card {
    position: absolute;
    left: 250px;
    width: 700px;
    height: 400px;
    border-radius: 3px;
    box-shadow: 0 6px 18px rgba(0,0,0,0.18);
  }
  .card--front {
    top: 90px;
    background: var(--paper);
    border-bottom: 4px solid var(--brand-blue);
  }
  .card--back {
    top: 560px;
    background: var(--card-blue);
    border-bottom: 4px solid var(--edge-light);
  }
  .brand-name {
    position: absolute;
    display: flex;
    align-items: center;
    gap: 12px;
    font-weight: 400;
    line-height: 1;
    white-space: nowrap;
  }
  .brand-name__circle {
    display: inline-block;
    border-radius: 50%;
    flex: none;
  }
  .card--front .brand-name {
    top: 62px;
    right: 48px;
    font-size: 38px;
    color: var(--brand-blue);
  }
  .card--front .brand-name__circle {
    width: 16px;
    height: 16px;
    background: var(--brand-blue);
  }
  .card--back .brand-name {
    top: 50%;
    left: 50%;
    transform: translate(-50%, -50%);
    font-size: 58px;
    color: var(--white);
  }
  .card--back .brand-name__circle {
    width: 22px;
    height: 22px;
    background: var(--white);
  }
  .contact-block {
    position: absolute;
    left: 56px;
    top: 118px;
  }
  .person-name {
    font-size: 30px;
    font-weight: 400;
    color: var(--brand-blue);
    line-height: 1.1;
  }
  .person-role {
    font-size: 16px;
    color: var(--ink-grey);
    margin-top: 2px;
  }
  .divider {
    width: 70px;
    height: 1.5px;
    background: var(--rule-grey);
    margin: 16px 0 14px;
  }
  .contact-list {
    list-style: none;
  }
  .contact-list li {
    display: flex;
    align-items: center;
    gap: 10px;
    font-size: 18px;
    color: var(--ink-grey);
    line-height: 26px;
  }
  .contact-list svg {
    width: 14px;
    height: 14px;
    flex: none;
    fill: var(--brand-blue);
  }
  .tagline {
    margin-top: 24px;
    font-size: 17px;
    color: var(--ink-grey);
  }
</style>
</head>
<body>
<main class="stage">
  <section class="card card--front" aria-label="Business card front">
    <div class="brand-name"><span class="brand-name__circle" aria-hidden="true"></span>FairlyNeat</div>
    <div class="contact-block">
      <h1 class="person-name">Marcus Thorne</h1>
      <p class="person-role">Co-Founder &amp; Chief Product Officer</p>
      <div class="divider"></div>
      <ul class="contact-list">
        <li>
          <svg viewBox="0 0 24 24" aria-hidden="true"><path d="M6.6 10.8a15.1 15.1 0 0 0 6.6 6.6l2.2-2.2c.3-.3.7-.4 1-.2 1.1.4 2.300.6 3.6.6.6 0 1 .4 1 1V20c0 .6-.4 1-1 1A17 17 0 0 1 3 4c0-.6.4-1 1-1h3.5c.6 0 1 .4 1 1 0 1.3.2 2.5.6 3.6.1.3 0 .7-.2 1z"/></svg>
          0279 183 640
        </li>
        <li>
          <svg viewBox="0 0 24 24" aria-hidden="true"><path d="M2 5h20v14H2z M4 7v.5l8 5 8-5V7l-8 5z" fill-rule="evenodd"/></svg>
          marcus@fairlyneat.nz
        </li>
        <li>
          <svg viewBox="0 0 24 24" aria-hidden="true"><circle cx="12" cy="12" r="10"/></svg>
          www.fairlyneat.nz
        </li>
      </ul>
      <p class="tagline">Shaping Labels With Heart</p>
    </div>
  </section>

  <section class="card card--back" aria-label="Business card back">
    <div class="brand-name"><span class="brand-name__circle" aria-hidden="true"></span>FairlyNeat</div>
  </section>
</main>
</body>
</html>
```